Boilerplate Management Organization Chart

"Our Management Approach is a deliberate step-by-step process and supports our Technical Approach detailed in proposal submission. The Management Approach covers all the human capital aspects for executing a contract—from contract award through to sustainment and/or transition of the contract to another company. It includes how we organize, hire, staff, train, and account for our contract employees—as well as their complete personal life-cycle management within the company."

We need this management approach to depict an amazing management process that demonstrates best practices of the project management body of knowledge. We need this vector image to be applicable to any proposal without making references to any other proposals. Generic names but using strong business language.
Updates

Thanks for all designs submitted thus far. Some have stuck to the original type of chart. We would like to see a completely different way to show the same information. It has to be able to be recognized and deciphered very quickly by people who might not necessarily want to look at it. It must draw them in and make it incredibly easy to distinguish a management approach that looks fresh, infallible, and easily implemented.

Target Market(s)

Federal space, Government organizations looking for procedural efficiencies,

Industry/Entity Type

Management

Requirements
Must have
• Must not take up more than 1/3 to 1/2 of printable page and be clear.
Should not have
• Not too much color, but should stick to some color palette of some interest.

```html
<!DOCTYPE html>
<html lang="en">
<head>
<meta charset="utf-8">
<title>Management Approach</title>
<link href="https://fonts.googleapis.com/css2?family=Didact+Gothic&family=Montserrat:wght@600;700&display=swap" rel="stylesheet">
<style>
  :root {
    --brand-dark: #0b68a8;
    --brand-light: #2aa3d8;
    --brand-title: #0d6db3;
    --label-ink: #4a4a4a;
    --line-ink: #666666;
    --rule: #b5b5b5;
    --page: #ffffff;
  }
  html, body { margin: 0; padding: 0; overflow: hidden; }
  body { background: var(--page); }
  .canvas {
    position: relative;
    width: 847px;
    height: 1200px;
    overflow: hidden;
    background: var(--page);
  }
  .diagram { position: absolute; left: 0; top: 0; }
  .title-banner {
    position: absolute;
    left: 242px; top: 97px;
    width: 430px; height: 42px;
    display: flex; align-items: center; justify-content: center;
    font-family: "Montserrat", sans-serif;
    font-weight: 700;
    font-size: 22px;
    color: #ffffff;
    letter-spacing: 0.2px;
  }
  .step-label {
    position: absolute;
    font-family: "Didact Gothic", sans-serif;
    font-size: 14px;
    line-height: 15px;
    color: var(--label-ink);
  }
  .step-label.to-left { text-align: right; }
  .evaluation-label {
    position: absolute;
    left: 271px; top: 611px;
    width: 300px;
    text-align: center;
    font-family: "Montserrat", sans-serif;
    font-weight: 700;
    font-size: 23px;
    color: var(--brand-title);
  }
  .section-rule {
    position: absolute;
    left: 0; top: 731px;
    width: 847px; height: 2px;
    background: var(--rule);
  }
</style>
</head>
<body>
<div class="canvas">
  <svg class="diagram" width="847" height="1200" viewBox="0 0 847 1200">
    <defs>
      <marker id="arrow-head" viewBox="0 0 10 10" refX="8" refY="5" markerWidth="6" markerHeight="6" orient="auto">
        <path d="M0,0 L10,5 L0,10 Z" fill="var(--line-ink)"/>
      </marker>
      <path id="ring-segment" d="M4.03,-153.95 A154,154 0 0 1 106,-111.7 L63.33,-66.73 A92,92 0 0 0 2.41,-91.97 Z"/>
    </defs>

    <!-- heading -->
    <polygon class="banner-bar" points="242,97 688,97 678,139 242,139" fill="var(--brand-title)"/>
    <polygon class="banner-accent" points="694,97 702,97 692,139 684,139" fill="var(--brand-light)"/>
    <circle class="badge-ring" cx="182" cy="117" r="41" fill="#ffffff"/>
    <circle class="badge" cx="182" cy="117" r="36" fill="var(--brand-light)"/>
    <g class="badge-icon" fill="#ffffff">
      <circle cx="182" cy="104" r="7"/>
      <rect x="172" y="113" width="20" height="22" rx="6"/>
      <circle cx="166" cy="109" r="5"/>
      <rect x="158" y="116" width="13" height="17" rx="5"/>
      <circle cx="198" cy="109" r="5"/>
      <rect x="193" y="116" width="13" height="17" rx="5"/>
    </g>

    <!-- process ring -->
    <g class="process-ring" transform="translate(424,384)">
      <g transform="rotate(0)">
        <use href="#ring-segment" fill="var(--brand-light)"/>
        <g transform="translate(47,-114) rotate(0)" fill="none" stroke="#fff" stroke-width="3">
          <circle r="9"/><circle r="3" fill="#fff"/>
        </g>
      </g>
      <g transform="rotate(45)">
        <use href="#ring-segment" fill="var(--brand-dark)"/>
        <g transform="translate(47,-114) rotate(-45)" fill="#fff">
          <circle r="8"/><circle r="3" fill="var(--brand-dark)"/>
          <rect x="-2.5" y="-12" width="5" height="24"/>
          <rect x="-12" y="-2.5" width="24" height="5"/>
          <rect x="-2.5" y="-12" width="5" height="24" transform="rotate(45)"/>
          <rect x="-2.5" y="-12" width="5" height="24" transform="rotate(-45)"/>
          <circle r="3.5" fill="var(--brand-dark)"/>
        </g>
      </g>
      <g transform="rotate(90)">
        <use href="#ring-segment" fill="var(--brand-light)"/>
        <g transform="translate(47,-114) rotate(-90)" fill="#fff">
          <circle cx="-10" r="5"/><circle r="6"/><circle cx="10" r="5"/>
        </g>
      </g>
      <g transform="rotate(135)">
        <use href="#ring-segment" fill="var(--brand-dark)"/>
        <g transform="translate(47,-114) rotate(-135)" fill="none" stroke="#fff" stroke-width="2.5">
          <rect x="-12" y="-10" width="24" height="16"/>
          <path d="M-6,12 L0,6 L6,12"/>
        </g>
      </g>
      <g transform="rotate(180)">
        <use href="#ring-segment" fill="var(--brand-light)"/>
        <g transform="translate(47,-114) rotate(-180)" fill="#fff">
          <rect x="-12" y="2" width="6" height="10"/>
          <rect x="-3" y="-4" width="6" height="16"/>
          <rect x="6" y="-10" width="6" height="22"/>
        </g>
      </g>
      <g transform="rotate(225)">
        <use href="#ring-segment" fill="var(--brand-dark)"/>
        <g transform="translate(47,-114) rotate(-225)" fill="none" stroke="#fff" stroke-width="3.5" stroke-linecap="round" stroke-linejoin="round">
          <path d="M-10,0 L-3,8 L11,-8"/>
        </g>
      </g>
      <g transform="rotate(270)">
        <use href="#ring-segment" fill="var(--brand-light)"/>
        <g transform="translate(47,-114) rotate(-270)">
          <circle r="11" fill="none" stroke="#fff" stroke-width="2.5"/>
          <text y="5" text-anchor="middle" font-family="Montserrat, sans-serif" font-weight="700" font-size="14" fill="#fff">$</text>
        </g>
      </g>
      <g transform="rotate(315)">
        <use href="#ring-segment" fill="var(--brand-dark)"/>
        <g transform="translate(47,-114) rotate(-315)" fill="none" stroke="#fff" stroke-width="2.5">
          <path d="M-10,2 A10,10 0 0 1 8,-6"/>
          <path d="M10,-2 A10,10 0 0 1 -8,6"/>
          <path d="M4,-9 L8,-6 L5,-2" />
          <path d="M-4,9 L-8,6 L-5,2" />
        </g>
      </g>
    </g>

    <!-- leader lines -->
    <g class="leaders" fill="none" stroke="var(--line-ink)" stroke-width="1.3" marker-end="url(#arrow-head)">
      <polyline points="360,230 352,213 310,213"/>
      <polyline points="490,230 498,213 536,213"/>
      <polyline points="574,325 590,305 612,305"/>
      <polyline points="574,445 592,460 612,460"/>
      <polyline points="486,530 490,546 551,546"/>
      <polyline points="356,526 350,546 293,546"/>
      <polyline points="290,440 278,456 274,456"/>
      <polyline points="275,315 260,305 231,305"/>
    </g>

    <!-- evaluation loop -->
    <g class="evaluation-loop" fill="none" stroke="var(--line-ink)" stroke-width="1.3">
      <circle cx="104" cy="381" r="2" fill="var(--line-ink)"/>
      <path d="M104,381 L64,381 Q53,381 53,392 L53,614 Q53,626 65,626 L265,626" marker-end="url(#arrow-head)"/>
      <circle cx="746" cy="381" r="2" fill="var(--line-ink)"/>
      <path d="M746,381 L788,381 Q800,381 800,392 L800,614 Q800,626 788,626 L580,626" marker-end="url(#arrow-head)"/>
    </g>
  </svg>

  <div class="title-banner">MANAGEMENT APPROACH</div>

  <div class="step-label to-left" style="right:540px; top:203px;">Sustainment /<br>Transition</div>
  <div class="step-label" style="left:540px; top:203px;">Responsibility<br>Fixed</div>
  <div class="step-label" style="left:617px; top:290px;">Management<br>&amp; Oversight</div>
  <div class="step-label" style="left:617px; top:445px;">Manning the<br>team</div>
  <div class="step-label" style="left:556px; top:539px;">Training</div>
  <div class="step-label to-left" style="right:559px; top:531px;">Professional<br>Development</div>
  <div class="step-label to-left" style="right:577px; top:441px;">Retention /<br>Quality of life</div>
  <div class="step-label to-left" style="right:620px; top:298px;">Benefits</div>

  <div class="evaluation-label">PROGRAM EVALUATION</div>
  <div class="section-rule"></div>
</div>
</body>
</html>
```